Birch Spire Kilo Marsh website

we need a website to cater to 2 aspect of the business. We have Birch spire residence and birch spire office. For the office, we will get their inquire and arrange a face to face meetup to show them the office area for rent. For the residence side, it will need to be like stayrio or velupa.com. we want to allow them to book online for the date they need. We have a total of 10 different room configurations starting at $70 per night and up depending on the size of the room. example of the design is https://lumbrahaven.com/

Target Market(s)

the website should have detail information on the layout, designs, and luxury of the building.

Industry/Entity Type

office and service appartment rental/lease

Coding

Coded - Design and coding required

Number of Pages Required

5+ page

Requirements
Must have
• a luxury perspective
Nice to have
• example https://lumbrahaven.com/

```html
<!DOCTYPE html>
<html lang="en">
<head>
<meta charset="utf-8">
<title>Birch Spire Kilo Marsh — Home</title>
<link href="https://fonts.googleapis.com/css2?family=Poppins:wght@600;700&family=Inter:wght@400;500;600;700&family=Marcellus&display=swap" rel="stylesheet">
<style>
:root{
  --red:#e0262f;
  --gold:#d49c2c;
  --ink:#161616;
  --body:#2a2a2a;
  --muted:#7a7a7a;
  --line:#d9d9d9;
  --white:#ffffff;
}
*{box-sizing:border-box;margin:0;padding:0}
html,body{width:806px;height:1200px;overflow:hidden;background:var(--white)}
body{position:relative;font-family:'Inter',sans-serif;color:var(--body)}
.abs{position:absolute}

/* header */
.brand{left:82px;top:8px;width:96px;text-align:center}
.brand-mark{display:block;margin:0 auto 4px;width:22px;height:22px;border:1.2px solid var(--gold)}
.brand-name{font-family:'Marcellus',serif;font-size:10px;color:var(--gold);white-space:nowrap;letter-spacing:.2px}
.nav{top:29px;left:345px;display:flex;font-size:8.6px;color:var(--ink)}
.nav a{color:inherit;text-decoration:none;position:absolute;white-space:nowrap}
.nav a.active{border-bottom:1px solid var(--ink);padding-bottom:1px;top:-1px}
.btn{display:flex;align-items:center;justify-content:center;font-weight:600;border-radius:3px;font-size:8.6px;white-space:nowrap}
.btn-red{background:var(--red);color:var(--white)}
.btn-gold{background:var(--gold);color:var(--white)}
.btn-ghost{border:1px solid var(--gold);color:var(--gold);background:var(--white)}
.nav-cta{left:635px;top:21px;width:92px;height:29px}

/* hero */
.hero{left:82px;top:78px;width:645px;height:254px;border-radius:9px;
  background:linear-gradient(100deg,#9c5f58 0%,#8a6a5f 40%,#a08d7c 65%,#5c4a3e 88%,#2e2620 100%)}
.eyebrow{top:122px;left:104px;width:266px;display:flex;align-items:center;gap:12px;font-family:'Marcellus',serif;font-size:13px;color:var(--white)}
.eyebrow::before,.eyebrow::after{content:"";flex:1;height:1px;background:rgba(255,255,255,.8)}
.hero-title{left:104px;top:138px;font-family:'Poppins',sans-serif;font-weight:700;font-size:33px;color:var(--white);white-space:nowrap}
.hero-sub{left:104px;top:176px;font-size:11px;font-weight:500;color:var(--white);letter-spacing:.1px}
.explore{left:104px;top:206px;width:89px;height:28px;gap:6px}

/* booking */
.booking{left:104px;top:281px;width:600px;height:101px;background:var(--white);border-radius:9px;box-shadow:0 6px 18px rgba(0,0,0,.12)}
.field-label{top:299px;font-size:8.6px;color:var(--ink);font-weight:500}
.field{top:315px;height:18px;border:1px solid #cfcfcf;border-radius:2px;font-size:7.2px;color:#8a8a8a;display:flex;align-items:center;justify-content:space-between;padding:0 7px}
.divider{top:295px;width:1px;height:42px;background:var(--line)}
.book-now{left:373px;top:348px;width:63px;height:21px;font-size:8px}
.search{left:662px;top:345px;width:24px;height:24px;border-radius:50%;background:#e4e4e4;display:flex;align-items:center;justify-content:center}

/* section heading */
.kicker{top:426px;left:307px;width:191px;display:flex;align-items:center;gap:12px;font-family:'Marcellus',serif;font-size:13px;color:var(--gold);white-space:nowrap}
.kicker::before,.kicker::after{content:"";flex:1;height:1px;background:#b9b9b9}
.section-title{top:442px;left:0;width:806px;text-align:center;font-family:'Poppins',sans-serif;font-weight:700;font-size:22.5px;color:var(--ink)}

/* rooms */
.room-photo{border-radius:9px}
.room-title{font-family:'Poppins',sans-serif;font-weight:600;font-size:19.5px;color:var(--ink);white-space:nowrap}
.reviews{font-size:7.6px;color:var(--muted)}
.reviews span{color:var(--gold);letter-spacing:.5px}
.room-desc{width:300px;font-size:8.3px;line-height:12.4px;color:var(--body)}
.price{font-size:10px;color:var(--muted);display:flex;align-items:baseline;gap:6px}
.price b{font-family:'Marcellus',serif;font-weight:400;font-size:23px;color:var(--gold)}
.specs{width:200px;font-size:9px}
.specs div{display:flex;height:17.8px;align-items:center}
.specs dt{width:70px;color:var(--ink)}
.specs dd{color:var(--muted)}
.room-btn{width:89px;height:28px;font-size:8.6px}

.view-all{left:362px;top:1106px;width:82px;height:28px}
.progress{left:182px;top:1156px;font-family:'Poppins',sans-serif;font-weight:700;font-size:21.5px;color:var(--ink)}
</style>
</head>
<body>

<header>
  <div class="abs brand"><span class="brand-mark"></span><span class="brand-name">Birch Spire Kilo Marsh</span></div>
  <nav class="abs nav">
    <a class="active" style="left:0">Home</a>
    <a style="left:47px">Residence</a>
    <a style="left:113px">About Us</a>
    <a style="left:174px">Offices</a>
    <a style="left:226px">Contact Us</a>
  </nav>
  <a class="abs btn btn-red nav-cta">Book Residence</a>
</header>

<section>
  <div class="abs hero" role="img" aria-label="Photo of the tower entrance facade with the building name in gold letters"></div>
  <div class="abs eyebrow">Get Luxury &amp; Comfort</div>
  <h1 class="abs hero-title">Welcome To Hotel</h1>
  <p class="abs hero-sub">THE PLACE WHERE ARE YOU LOOKING TO</p>
  <a class="abs btn btn-gold explore">Explore Now
    <svg width="10" height="9" viewBox="0 0 10 9" fill="none" stroke="#fff" stroke-width="1.3"><path d="M0 4.5h9M5.5 1l3.5 3.5L5.5 8"/></svg>
  </a>

  <form class="abs booking"></form>
  <span class="abs field-label" style="left:123px">Email</span>
  <span class="abs field" style="left:123px;width:96px">Your Email</span>
  <i class="abs divider" style="left:231px"></i>
  <span class="abs field-label" style="left:243px">Types Of Rooms</span>
  <span class="abs field" style="left:243px;width:96px">Select Room<svg width="7" height="4" viewBox="0 0 7 4" fill="none" stroke="#555"><path d="M.5.5l3 3 3-3"/></svg></span>
  <i class="abs divider" style="left:351px"></i>
  <span class="abs field-label" style="left:364px">Check In</span>
  <span class="abs field" style="left:364px;width:89px">05 Nov 2024<svg width="7" height="4" viewBox="0 0 7 4" fill="none" stroke="#555"><path d="M.5.5l3 3 3-3"/></svg></span>
  <i class="abs divider" style="left:464px"></i>
  <span class="abs field-label" style="left:477px">Check Out</span>
  <span class="abs field" style="left:477px;width:89px">12 Nov 2024<svg width="7" height="4" viewBox="0 0 7 4" fill="none" stroke="#555"><path d="M.5.5l3 3 3-3"/></svg></span>
  <i class="abs divider" style="left:578px"></i>
  <span class="abs field-label" style="left:590px">Types Of Offices</span>
  <span class="abs field" style="left:590px;width:96px">Select Office<svg width="7" height="4" viewBox="0 0 7 4" fill="none" stroke="#555"><path d="M.5.5l3 3 3-3"/></svg></span>
  <a class="abs btn btn-red book-now">Book Now</a>
  <span class="abs search"><svg width="11" height="11" viewBox="0 0 11 11" fill="none" stroke="#555" stroke-width="1.1"><circle cx="4.7" cy="4.7" r="3.9"/><path d="M7.6 7.6l2.8 2.8"/></svg></span>
</section>

<section>
  <div class="abs kicker">About Us</div>
  <h2 class="abs section-title">Discover Our Rooms</h2>

  <div class="abs room-photo" style="left:82px;top:503px;width:311px;height:251px;background:linear-gradient(120deg,#d9b469 0%,#e8d9b8 40%,#c9a77a 70%,#8f6a52 100%)" role="img" aria-label="Photo of a bright deluxe bedroom with a white bed and tall windows"></div>
  <h3 class="abs room-title" style="left:420px;top:514px">Luxury Super Delux</h3>
  <p class="abs reviews" style="left:420px;top:541px">Reviews <span>★★★★★</span></p>
  <p class="abs room-desc" style="left:420px;top:557px">Lorem Ipsum is simply dummy text of the printing and typesetting industry. Lorem Ipsum has been the industry's standard dummy text ever since the 1500s</p>
  <p class="abs price" style="left:420px;top:594px">Starting Price <b>$70</b> /Night</p>
  <dl class="abs specs" style="left:420px;top:623px">
    <div><dt>Status</dt><dd>Active</dd></div>
    <div><dt>Payment</dt><dd>$70 Approved</dd></div>
    <div><dt>Guest</dt><dd>3</dd></div>
    <div><dt>Beds</dt><dd>3</dd></div>
  </dl>
  <a class="abs btn btn-gold room-btn" style="left:420px;top:709px">Book Now</a>
  <a class="abs btn btn-ghost room-btn" style="left:517px;top:709px">More Info</a>

  <h3 class="abs room-title" style="left:82px;top:828px">Luxury Family Delux</h3>
  <p class="abs reviews" style="left:82px;top:855px">Reviews <span>★★★★★</span></p>
  <p class="abs room-desc" style="left:82px;top:871px">Lorem Ipsum is simply dummy text of the printing and typesetting industry. Lorem Ipsum has been the industry's standard dummy text ever since the 1500s</p>
  <p class="abs price" style="left:82px;top:908px">Starting Price <b>$90</b> /Night</p>
  <dl class="abs specs" style="left:82px;top:937px">
    <div><dt>Status</dt><dd>Active</dd></div>
    <div><dt>Payment</dt><dd>$90 Approved</dd></div>
    <div><dt>Guest</dt><dd>2</dd></div>
    <div><dt>Beds</dt><dd>2</dd></div>
  </dl>
  <a class="abs btn btn-gold room-btn" style="left:82px;top:1023px">Book Now</a>
  <a class="abs btn btn-ghost room-btn" style="left:179px;top:1023px">More Info</a>
  <div class="abs room-photo" style="left:415px;top:809px;width:312px;height:266px;background:linear-gradient(150deg,#6b4a2c 0%,#c08a3e 35%,#e6b25a 55%,#7a5230 80%,#2e1e14 100%)" role="img" aria-label="Photo of an ornate golden family suite with a large bed and sunset windows"></div>

  <a class="abs btn btn-red view-all">View All</a>
  <h2 class="abs progress">In Progress</h2>
</section>

</body>
</html>
```